Build a Website for Pharmacy Stores company

We are looking to build a modern website for our Pharmacy Stores.

The goal of the website is to inform customers about us, our locations, blog posts, promotion section, etc..
We are thinking of having the homepage as a digest of all the pages. Please see attached suggested pages and their descriptions.

Design: creative, clean and modern; similar to material design is nice! Should have some professional feel to it. No cheap design, no ready made templates!
Color scheme should match the logo (color green with some grey) make it work! Don't style the pages around the old logo as it is about to be replaced.

Development: Dynamic content, wordpress preferred, must be responsive, mobile friendly.

Please do not submit generic templates as your submission, you will be disqualified.

```html
<!DOCTYPE html>
<html lang="en">
<head>
<meta charset="utf-8">
<title>Verdana Care Pharmacies – Our Values</title>
<link rel="stylesheet" href="https://fonts.googleapis.com/css2?family=Poppins:wght@300;400;500;600&display=swap">
<style>
  :root {
    --green: #7ab829;
    --green-soft: #cfe6b0;
    --grey-dark: #333333;
    --grey-text: #666666;
    --grey-muted: #8a8a8a;
    --grey-line: #9a9a9a;
    --band: #f5f5f5;
    --white: #ffffff;
  }
  * { margin: 0; padding: 0; box-sizing: border-box; }
  html, body { width: 1200px; height: 4785px; overflow: hidden; background: var(--white); }
  body { font-family: "Poppins", sans-serif; color: var(--grey-dark); position: relative; }

  .site-header { position: absolute; top: 0; left: 0; width: 1200px; height: 175px; }
  .brand { position: absolute; left: 75px; top: 55px; display: flex; align-items: center; gap: 18px; }
  .brand-dot { width: 60px; height: 60px; border-radius: 50%; background: var(--green); }
  .brand-name { font-size: 30px; font-weight: 600; color: var(--green); letter-spacing: .5px; }
  .language-toggle {
    position: absolute; left: 712px; top: 50px; width: 240px; height: 76px;
    border: 4px solid var(--green); border-radius: 40px;
    display: flex; align-items: center; justify-content: center; gap: 12px;
    font-size: 27px; color: var(--grey-dark);
  }
  .menu-toggle { position: absolute; left: 1062px; top: 62px; width: 60px; }
  .menu-toggle span { display: block; height: 9px; background: var(--grey-dark); border-radius: 2px; margin-bottom: 10px; }

  .hero {
    position: absolute; top: 175px; left: 0; width: 1200px; height: 775px;
    background:
      linear-gradient(180deg, rgba(255,255,255,0) 78%, #fff 100%),
      linear-gradient(100deg, #e9eef0 0%, #3bbf95 18%, #f1f3f4 30%, #e8e4ee 50%, #f4f1f5 70%, #dfe9ec 100%);
  }

  .values-intro {
    position: absolute; top: 1012px; left: 0; width: 1200px; height: 513px;
    background: var(--band); text-align: center;
  }
  .values-title { margin-top: 110px; font-size: 68px; font-weight: 300; color: var(--grey-dark); line-height: 1.2; }
  .values-title strong { font-weight: 600; }
  .title-rule { display: flex; justify-content: center; gap: 30px; margin-top: 30px; }
  .title-rule .accent { width: 70px; height: 6px; background: var(--green); }
  .title-rule .base { width: 175px; height: 6px; background: var(--grey-line); }
  .values-lead { margin: 40px auto 0; width: 1080px; font-size: 26px; line-height: 45px; color: var(--grey-text); }

  .value { position: absolute; left: 0; width: 1200px; text-align: center; }
  .value-icon {
    width: 190px; height: 190px; margin: 0 auto; border-radius: 50%; background: var(--white);
    box-shadow: 0 4px 14px rgba(0,0,0,.08);
    display: flex; align-items: center; justify-content: center;
  }
  .value-icon svg { width: 100px; height: 100px; fill: var(--green); }
  .value-name { margin-top: 55px; font-size: 40px; font-weight: 500; color: var(--grey-text); letter-spacing: 1px; }
  .value-text { margin: 30px auto 0; width: 460px; font-size: 31px; line-height: 50px; color: var(--grey-muted); }
</style>
</head>
<body>
  <header class="site-header">
    <div class="brand">
      <span class="brand-dot"></span>
      <span class="brand-name">VERDANA CARE PHARMACIES</span>
    </div>
    <div class="language-toggle">Language
      <svg width="18" height="12" viewBox="0 0 18 12"><path d="M2 2l7 7 7-7" fill="none" stroke="#333" stroke-width="3"/></svg>
    </div>
    <div class="menu-toggle"><span></span><span></span><span></span></div>
  </header>

  <div class="hero" role="img" aria-label="Photo of bright pharmacy shelves stocked with medicine boxes"></div>

  <section class="values-intro">
    <h2 class="values-title">Our <strong>Values</strong></h2>
    <div class="title-rule"><span class="accent"></span><span class="base"></span></div>
    <p class="values-lead">It is a long established fact that a reader will be distracted by the readable content of a page when looking at its less sed to using 'Content as their default model text, and a search for 'lorem ipsum'</p>
  </section>

  <article class="value" style="top:1422px">
    <div class="value-icon">
      <svg viewBox="0 0 100 100"><path d="M4 30l18-8 14 6 12-6 14 4 16-6 18 10-8 22-8 4-22 18c-4 3-8 2-10-1-3 2-7 1-9-2-3 1-6 0-8-3-3 0-6-2-6-5L10 52zM40 36l-10 10c-2 2 0 5 3 4l12-9 20 16c3 2 6-1 4-4L50 40z"/></svg>
    </div>
    <h3 class="value-name">Integrity</h3>
    <p class="value-text">Here are many variations of passages Lorem Ipsum available.</p>
  </article>

  <article class="value" style="top:2322px">
    <div class="value-icon">
      <svg viewBox="0 0 100 100"><path d="M50 56L30 36c-8-8 2-22 12-16l8 6 8-6c10-6 20 8 12 16z"/><path d="M6 30c4 0 6 3 6 6v18l18 16c4 4 6 8 6 12v12H24V84L6 66z"/><path d="M94 30c-4 0-6 3-6 6v18L70 70c-4 4-6 8-6 12v12h12V84l18-18z"/></svg>
    </div>
    <h3 class="value-name">Compassion</h3>
    <p class="value-text">Here are many variations of passages Lorem Ipsum available.</p>
  </article>

  <article class="value" style="top:3222px">
    <div class="value-icon">
      <svg viewBox="0 0 100 100"><circle cx="50" cy="24" r="14"/><path d="M22 50c6-8 16-10 28-10s22 2 28 10l8 26H14zM10 80h80v10H10z"/></svg>
    </div>
    <h3 class="value-name">Respect</h3>
    <p class="value-text">Here are many variations of passages Lorem Ipsum available.</p>
  </article>

  <article class="value" style="top:4122px">
    <div class="value-icon">
      <svg viewBox="0 0 100 100"><path d="M50 4l9 6 11 0 3 10 9 7-4 10 4 10-9 7-3 10-11 0-9 6-9-6-11 0-3-10-9-7 4-10-4-10 9-7 3-10 11 0z"/><circle cx="50" cy="37" r="14" fill="#fff"/><circle cx="50" cy="37" r="9"/><path d="M38 72h24v26l-12-8-12 8z"/></svg>
    </div>
    <h3 class="value-name">Professionalism</h3>
    <p class="value-text">Here are many variations of passages Lorem Ipsum available.</p>
  </article>
</body>
</html>
```